Business card for new business.
Red and black corporate colors.
Card can have an Indsutrial feel to it. Feel free to add Rust, Bolted steel, or graphics as you see fit. We provide highly specialized services to the below mentioned industries.
Keep information out of corners so that if I want I can choose rounded corners.
Information
- front. name - title - phone - email
- Rear
Refining - Rail - Infrastructure - Mining - Energy
Ashford - Brookvale - Port Kessler - Redmont - Westhaven

```html
<!DOCTYPE html>
<html lang="en">
<head>
<meta charset="utf-8">
<title>Framewell business card</title>
<link href="https://fonts.googleapis.com/css2?family=Michroma&family=Montserrat:wght@500;600;800&family=Roboto:wght@400;500&display=swap" rel="stylesheet">
<style>
  :root {
    --page: #f1f1f1;
    --charcoal: #2b2b2d;
    --steel-light: #f4f4f4;
    --steel-mid: #dcdcdc;
    --red: #e31b23;
    --badge-grey: #a8a8a8;
    --text-light: #ffffff;
    --text-soft: #e6e6e6;
    --logo-dark: #2a2a2a;
    --logo-grey: #bdbdbd;
  }
  * { margin: 0; padding: 0; box-sizing: border-box; }
  html, body { width: 1200px; height: 881px; overflow: hidden; background: var(--page); }
  .canvas { position: relative; width: 1200px; height: 881px; }

  .card {
    position: absolute; top: 286px; width: 540px; height: 309px;
    overflow: hidden; box-shadow: 0 6px 18px rgba(0,0,0,.18);
  }
  .card--front { left: 40px; }
  .card--back  { left: 620px; background: var(--charcoal); }

  /* Front */
  .front__steel {
    position: absolute; left: 0; top: 0; width: 51%; height: 100%;
    background: radial-gradient(ellipse at 30% 30%, var(--steel-light), var(--steel-mid));
  }
  .front__logo {
    position: absolute; left: 0; width: 250px; top: 140px; text-align: center;
    font-family: "Montserrat", sans-serif; font-weight: 800; font-size: 25px;
    letter-spacing: 1px; color: var(--logo-dark);
  }
  .front__panel {
    position: absolute; left: 51%; top: 0; right: 0; height: 100%;
    background: var(--charcoal);
  }
  .front__badges { position: absolute; left: 251px; top: 40px; }
  .front__details {
    position: absolute; left: 330px; top: 54px; width: 180px;
    font-family: "Roboto", sans-serif; color: var(--text-soft); font-size: 12px; line-height: 15.5px;
  }
  .front__name {
    font-family: "Michroma", sans-serif; font-size: 16px; color: var(--text-light);
    letter-spacing: 1px; line-height: 22px;
  }
  .front__title { color: var(--red); font-size: 11.5px; margin-bottom: 27px; }
  .front__group { padding: 4px 0 7px; }
  .front__group + .front__group { border-top: 1.5px solid var(--red); }

  /* Back */
  .back__wordmark {
    position: absolute; left: 0; right: 0; top: 82px; text-align: center;
    font-family: "Montserrat", sans-serif; font-weight: 800; font-size: 50px;
    color: var(--logo-grey); letter-spacing: 1px;
  }
  .back__industries {
    position: absolute; left: 0; right: 0; top: 190px; text-align: center;
    font-family: "Montserrat", sans-serif; font-weight: 600; font-size: 14px;
    color: var(--text-soft); letter-spacing: .3px;
  }
  .back__band {
    position: absolute; left: 0; right: 0; bottom: 0; height: 62px;
    background: linear-gradient(180deg, #16171a, #3a3d44 60%, #1b1c1f);
    border-top: 2px solid var(--red);
  }
  .back__tab {
    position: absolute; left: 50%; top: 0; transform: translateX(-50%);
    width: 190px; height: 8px; background: var(--red);
    clip-path: polygon(0 0, 100% 0, 95% 100%, 5% 100%);
  }
  .back__cities {
    position: absolute; left: 0; right: 0; top: 26px; text-align: center;
    font-family: "Montserrat", sans-serif; font-weight: 600; font-size: 12.5px; color: var(--text-light);
  }
</style>
</head>
<body>
<main class="canvas">

  <section class="card card--front" aria-label="Card front">
    <div class="front__steel"></div>
    <div class="front__logo">FRAMEWELL</div>
    <div class="front__panel"></div>

    <svg class="front__badges" width="56" height="230" viewBox="0 0 56 230" aria-hidden="true">
      <polygon points="28,2 52,16 52,44 28,58 4,44 4,16" fill="var(--badge-grey)"/>
      <polygon points="28,72 50,88 50,208 28,224 6,208 6,88" fill="var(--red)"/>
      <!-- bell -->
      <path d="M22 108 q0-12 6-12 q6 0 6 12 v3 l3 3 h-18 l3-3z" fill="#fff"/>
      <circle cx="28" cy="117" r="2" fill="#fff"/>
      <line x1="21" y1="128" x2="35" y2="128" stroke="#fff" stroke-width="1.2"/>
      <!-- browser window -->
      <rect x="19" y="138" width="18" height="13" fill="none" stroke="#fff" stroke-width="1.5"/>
      <line x1="19" y1="142" x2="37" y2="142" stroke="#fff" stroke-width="1.5"/>
      <line x1="21" y1="162" x2="35" y2="162" stroke="#fff" stroke-width="1.2"/>
      <!-- location pin -->
      <path d="M28 186 l-5-8 a6 6 0 1 1 10 0 z" fill="#fff"/>
      <circle cx="28" cy="175" r="2.2" fill="var(--red)"/>
      <rect x="20" y="189" width="16" height="3" fill="#fff"/>
    </svg>

    <div class="front__details">
      <div class="front__name">JOHN DOE</div>
      <div class="front__title">Managing Director</div>
      <div class="front__group">222-222-2222<br>333-333-3333</div>
      <div class="front__group">john@framewell.com<br>www.framewell.com</div>
      <div class="front__group">1234 Street name, City name<br>Your Country, Zip Code.</div>
    </div>
  </section>

  <section class="card card--back" aria-label="Card back">
    <div class="back__wordmark">FRAMEWELL</div>
    <div class="back__industries">REFINING · RAIL · INFRASTRUCTURE · MINING · ENERGY</div>
    <div class="back__band">
      <div class="back__tab"></div>
      <div class="back__cities">Ashford - Brookvale - Port Kessler - Redmont - Westhaven</div>
    </div>
  </section>

</main>
</body>
</html>
```